Specialist Executive Search firm needs new MS Word template(and other templates to match eventually)

Corvel Associates a boutique Executive Search and Recruitment firm, recruiting senior specialist advisors in the fields of Audit, Advisory, Tax Accounting, Corporate Finance and Law. The majority of our clients are professional services firms, i.e. Accounting firms and Law firms.

The ‘Research List / Market Map’ document we currently use to produce and then present to clients is a "long list" of candidates or prospective target candidates. It is a bit dated, and the formatting can be fiddly. So we would like someone to freshen it up and simplify it so that is functions much more effectively as a usable, consistent Template and it needs to be in MS Word. We are looking for something simple and contemporary, but professional, given the nature of our clients - usually Managing Partners or very Senior Partners - in Accounting and Law firms. We need it to be easy to use, so that we can just copy and paste information into it without the formatting requiring constant adjustment and checking.

The "usual" sequence of the document:

- Cover page - includes the name of the company we are sending it to, the role we are recruiting for, and a sketch of the city the role is in (or similar other sketch). The Corvel Associates brand is also featured.
- Confidentiality summary page,
- Table of contents - we would like this to be automated so that page numbers adjusted automatically to be accurate with contents page
- Project summary - usually 1 to 2 pages summarising the purpose of the project and the content of the document
- "Highlighted Candidates" page, which are targets / candidates we think are likely of particular interest to our client.
- Then a page or number of pages (depending on the nature of the search, this is sometimes up to 5 to 6 pages for each and every firm….with an average of 3/4 individuals per page. Other times, it may be just one individual per employer/firm) listed by firm with the following details of each candidate:
- Photo of target individual
- Name of individual
- Job title
- Location
- Summary of the individual and their experience, which can be between 1-2 paragraphs.

We are open to suggestions with respect to the above, i.e. improved format / layout / order of information.

We currently group target candidates by the firm that currently employs each. Each firm has the heading and we like them grouped this way, as do our clients as it assists with seeking feedback / market information from various stakeholders inside the client. We tend to group very large firms (TbR, LHNQ, Varnsby, QO) at the beginning of each market document, followed by large international mid tier firms, followed by quality boutiques and smaller firms. Whilst it can vary somewhat, generally speaking the larger firms are comprised of a larger number of potential targets than smaller firms. For obvious reasons.

I have attached an example of what we currently have, but please bear in mind this is a mock up for confidentiality reasons. I haven't included the confidentiality summary page, or the project summary either. Ideally for integration purposes, and to make it simpler to copy data from our CRM system and paste into the document, there will be a hidden table for the candidate information.

We also want a new font, as the one we have (DIN) needs to be downloaded by each user and if we send the document in MS Word format, the formatting can be totally unreadable to the recipient or at the very least can impact the layout and format. So perhaps a simple font that we can use as part of our brand, but that still looks smart and contemporary.

Once we finalise this word template, we will need to match it with our other proposal documents, terms of business, powerpoint templates etc, and we also need to refresh/redo our website.

I only work two days per week so it's a long time between me reviewing designs, and discussing with the Partners of the business.

Target Market(s)

Professional services firms, Director and Partner level

Industry/Entity Type

Recruitment

Font styles to use
Other font styles liked:
• Currently use DIN but keen for a different signature font to suit

Requirements
Must have
• Must be simple to copy and paste text from our other system, and our business colours which are dark brown and dark red - RGB codes to come shortly

```html
<!DOCTYPE html>
<html lang="en">
<head>
<meta charset="utf-8">
<title>Corvel Associates – Report Template</title>
<link href="https://fonts.googleapis.com/css2?family=Raleway:ital,wght@0,400;0,500;0,600;0,700;0,800;1,400&display=swap" rel="stylesheet">
<style>
:root{
  --canvas:#808080;
  --paper:#ffffff;
  --brown:#5a1f1a;
  --red:#c1272d;
  --ink:#3a3a3a;
  --muted:#777777;
  --numeral:#cfcfcf;
  --card:#f0f0f0;
  --rule:#dddddd;
  --row:#efefef;
}
*{box-sizing:border-box;margin:0;padding:0}
html,body{width:686px;height:1200px;overflow:hidden}
body{background:var(--canvas);font-family:"Raleway",sans-serif;color:var(--ink);position:relative}

.page{position:absolute;width:295px;height:221px;background:var(--paper);box-shadow:0 6px 10px rgba(0,0,0,.35);overflow:hidden}
.col-left{left:37px}.col-right{left:354px}
.row-1{top:116px}.row-2{top:366px}.row-3{top:614px}.row-4{top:863px}

.page-title{position:absolute;left:19px;top:13px;font-weight:800;font-size:12.5px;line-height:1.25;color:var(--ink);letter-spacing:.2px}
.page-title.firm{color:var(--brown);font-size:12.5px}
.title-rule{position:absolute;left:19px;width:35px;height:1px;background:var(--red)}

.brand{position:absolute;font-family:"Raleway",sans-serif;font-weight:800;color:var(--brown);text-align:right;line-height:.95;letter-spacing:-.2px}
.brand-small{right:16px;top:12px;font-size:8px}
.brand-large{font-size:13px}

.footer-rule{position:absolute;left:11px;right:11px;top:208px;height:.5px;background:var(--rule)}
.page-number{position:absolute;left:11px;top:212px;font-size:3px;color:var(--muted)}
.offices{position:absolute;right:11px;top:210px;text-align:right;font-size:3px;line-height:4px;color:var(--muted)}
.offices .web{color:var(--red)}

.sketch{position:absolute}

/* cover */
.cover-sketch{left:8px;top:8px;width:278px;height:146px;background:linear-gradient(180deg,#ecdfe2 0%,#ddc5c9 45%,#b9a9a4 70%,#a9b1ab 100%)}
.cover-title{position:absolute;left:18px;top:163px;font-weight:800;font-size:12px;color:var(--brown)}
.cover-line{position:absolute;left:18px;font-size:5.5px;font-weight:600;color:var(--brown)}
.cover-date{position:absolute;left:18px;top:205px;font-size:5.5px;font-style:italic;color:var(--red)}
.cover .brand-large{right:10px;top:165px}
.cover .offices{top:202px}

/* contents */
.toc{position:absolute;left:18px;top:40px;width:258px;border-collapse:collapse;table-layout:fixed}
.toc td{height:6.95px;font-size:2.8px;line-height:2.8px;padding:0 3px;border:.4px solid #9a9a9a}
.toc .section{width:64px;background:var(--red);color:#fff;font-weight:600;border-color:var(--red)}
.toc .entry{width:108px;background:var(--row)}
.toc .entry span::before{content:"•";margin:0 4px 0 1px}
.toc .num{text-align:right;background:#fff}

/* summary */
.summary-body{position:absolute;left:22px;top:49px;width:252px;font-size:4.8px;line-height:6.35px;text-align:justify;color:var(--ink)}
.summary-body p{margin-bottom:4px}
.summary-body ul{list-style:none;margin-bottom:4px}
.summary-body li{position:relative;padding-left:9px;margin-bottom:4.6px}
.summary-body li::before{content:"•";position:absolute;left:0}

/* notable */
.callout{position:absolute;left:19px;top:56px;width:257px;height:31px;background:var(--red);color:#fff;font-weight:700;font-size:5.4px;line-height:6.6px;padding:8.5px 7px;text-align:justify}
.highlight{position:absolute;width:110px}
.highlight .numeral{position:absolute;left:0;top:-3px;font-weight:800;font-size:12px;color:var(--numeral)}
.highlight h3{margin-left:26px;font-size:5.5px;font-weight:700;color:var(--ink)}
.highlight p{margin-left:26px;font-size:4.8px;line-height:6px;color:var(--muted);margin-top:1px}

/* candidates */
.candidate{position:absolute;left:18.5px;width:261.5px;height:48px;background:var(--card)}
.portrait{position:absolute;left:10px;top:7.5px;width:33px;height:33px;border-radius:50%;border:1.3px solid var(--red);background:radial-gradient(circle at 50% 40%,#d9d9d9 0%,#9a9a9a 60%,#5d5d5d 100%)}
.candidate-name{position:absolute;left:52px;top:10px;font-size:5.4px;font-weight:700;color:var(--ink)}
.candidate-role{position:absolute;left:52px;top:20.5px;font-size:5.4px;color:var(--red)}
.candidate-location{position:absolute;left:52px;top:31px;font-size:5.4px;font-style:italic;color:var(--muted)}
.candidate-bio{position:absolute;left:110px;top:0;width:144px;height:48px;display:flex;flex-direction:column;justify-content:center;font-size:2.8px;line-height:3.3px;color:var(--ink)}
.candidate-bio p+p{margin-top:2.5px}

/* closing */
.closing-sketch{left:9px;top:8.5px;width:276px;height:167.5px;background:linear-gradient(180deg,#e6edf3 0%,#d8dde0 30%,#cfae66 55%,#a9793f 75%,#b9b6b0 100%)}
.closing-title{position:absolute;left:18px;top:183px;font-weight:800;font-size:12.5px;line-height:14.5px;color:var(--brown)}
.closing .brand-large{right:11px;top:187px}
</style>
</head>
<body>

<!-- Cover -->
<section class="page cover col-left row-1">
  <div class="sketch cover-sketch" role="img" aria-label="Pink-toned sketch of the Sydney harbour skyline and opera house"></div>
  <h1 class="cover-title">REPORT</h1>
  <p class="cover-line" style="top:185px">Partner Corporate Tax – Sydney</p>
  <p class="cover-line" style="top:197px">Prepared for “Client”</p>
  <p class="cover-date">9 March 2020</p>
  <div class="brand brand-large">corvel<br>associates</div>
  <div class="offices">London | Dubai | Melbourne | St Helier | Sydney<br><span class="web">www.corvelassociates.net</span></div>
</section>

<!-- Contents -->
<section class="page col-right row-1">
  <h2 class="page-title">CONTENTS</h2>
  <div class="brand brand-small">corvel<br>associates</div>
  <table class="toc">
    <tr><td class="section">Summary</td><td class="entry"></td><td class="num">3</td></tr>
    <tr><td class="section">Notable Individuals / Firms</td><td class="entry"></td><td class="num">4</td></tr>
    <tr><td class="section">Corporate Tax Partners</td><td class="entry"></td><td class="num">6</td></tr>
    <tr><td class="section">Big 4 Firms</td><td class="entry"><span>Varnsby</span></td><td class="num">7</td></tr>
    <tr><td class="section"></td><td class="entry"><span>QO</span></td><td class="num">9</td></tr>
    <tr><td class="section"></td><td class="entry"><span>LHNQ</span></td><td class="num">10</td></tr>
    <tr><td class="section"></td><td class="entry"><span>TbR</span></td><td class="num">11</td></tr>
    <tr><td class="section">Mid Tier Firms</td><td class="entry"><span>Brannock</span></td><td class="num">12</td></tr>
    <tr><td class="section"></td><td class="entry"><span>Halden</span></td><td class="num">15</td></tr>
    <tr><td class="section"></td><td class="entry"><span>Marrow Hill</span></td><td class="num">16</td></tr>
    <tr><td class="section"></td><td class="entry"><span>Crane Wexley</span></td><td class="num">17</td></tr>
    <tr><td class="section"></td><td class="entry"><span>Grove Thatcher</span></td><td class="num">18</td></tr>
    <tr><td class="section"></td><td class="entry"><span>Hale Chesney</span></td><td class="num">20</td></tr>
    <tr><td class="section"></td><td class="entry"><span>HMR Lowe Tandy</span></td><td class="num">21</td></tr>
    <tr><td class="section"></td><td class="entry"><span>Kessel + Partners</span></td><td class="num">23</td></tr>
    <tr><td class="section"></td><td class="entry"><span>Marvane</span></td><td class="num">24</td></tr>
    <tr><td class="section"></td><td class="entry"><span>Novira</span></td><td class="num">25</td></tr>
    <tr><td class="section"></td><td class="entry"><span>Palmer Reach</span></td><td class="num">26</td></tr>
    <tr><td class="section"></td><td class="entry"><span>PRV</span></td><td class="num">27</td></tr>
    <tr><td class="section"></td><td class="entry"><span>RTN</span></td><td class="num">28</td></tr>
    <tr><td class="section"></td><td class="entry"><span>UVK Hollis Norland</span></td><td class="num">29</td></tr>
    <tr><td class="section"></td><td class="entry"><span>Wilton Barr</span></td><td class="num">30</td></tr>
    <tr><td class="section"></td><td class="entry"><span>Other</span></td><td class="num">31</td></tr>
  </table>
  <div class="footer-rule"></div>
  <span class="page-number">2</span>
  <div class="offices">London | Dubai | Melbourne | St Helier | Sydney<br><span class="web">www.corvelassociates.net</span></div>
</section>

<!-- Summary 1 -->
<section class="page col-left row-2">
  <h2 class="page-title">SUMMARY</h2>
  <div class="title-rule" style="top:28px"></div>
  <div class="brand brand-small">corvel<br>associates</div>
  <div class="summary-body">
    <p>Lorem ipsum dolor sit amet, consectetur adipiscing elit, sed do eiusmod tempor incididunt ut labore et dolore magna aliqua. Ut enim ad minim veniam, quis nostrud exercitation ullamco laboris nisi ut aliquip ex ea commodo consequat. Duis aute irure dolor in reprehenderit in voluptate velit esse cillum dolore eu fugiat nulla pariatur. Excepteur sint occaecat cupidatat non proident, sunt in culpa qui officia deserunt mollit anim id est laborum et dolorum fuga.</p>
    <p>Sed ut perspiciatis unde omnis iste natus error sit voluptatem accusantium doloremque laudantium, totam rem aperiam, eaque ipsa quae ab illo inventore veritatis et quasi architecto beatae vitae dicta sunt explicabo. Nemo enim ipsam voluptatem quia voluptas sit aspernatur aut odit aut fugit, sed quia consequuntur magni dolores eos qui ratione voluptatem sequi nesciunt. Neque porro quisquam est, qui dolorem ipsum quia dolor sit amet, consectetur, adipisci velit, sed quia non numquam eius modi tempora incidunt ut labore et dolore magnam aliquam quaerat voluptatem, ut enim ad minima veniam.</p>
    <p>Quis autem vel eum iure reprehenderit qui in ea voluptate velit esse quam nihil molestiae consequatur, vel illum qui dolorem eum fugiat quo voluptas nulla pariatur. At vero eos et accusamus et iusto odio dignissimos ducimus qui blanditiis praesentium.</p>
    <p>Nam libero tempore, cum soluta nobis est eligendi optio cumque nihil impedit quo minus id quod maxime placeat facere possimus, omnis voluptas assumenda est, omnis dolor repellendus temporibus autem.</p>
  </div>
  <div class="footer-rule"></div>
  <span class="page-number">3</span>
  <div class="offices">London | Dubai | Melbourne | St Helier | Sydney<br><span class="web">www.corvelassociates.net</span></div>
</section>

<!-- Summary 2 -->
<section class="page col-right row-2">
  <h2 class="page-title">SUMMARY</h2>
  <div class="title-rule" style="top:28px"></div>
  <div class="brand brand-small">corvel<br>associates</div>
  <div class="summary-body" style="top:47px">
    <ul>
      <li>Lorem ipsum dolor sit amet, consectetur adipiscing elit sed do eiusmod tempor.</li>
      <li>Ut enim ad minim veniam, quis nostrud exercitation ullamco laboris nisi ut aliquip ex ea commodo consequat duis aute irure dolor in reprehenderit.</li>
      <li>Excepteur sint occaecat cupidatat non proident, sunt in culpa qui officia deserunt mollit anim id est laborum, remaining essentially unchanged.</li>
      <li>Sed ut perspiciatis unde omnis iste natus error sit voluptatem accusantium doloremque laudantium, totam rem aperiam eaque ipsa quae ab illo inventore veritatis.</li>
    </ul>
    <p>Nemo enim ipsam voluptatem quia voluptas sit aspernatur aut odit aut fugit, sed quia consequuntur magni dolores eos qui ratione voluptatem sequi nesciunt. Neque porro quisquam est, qui dolorem ipsum quia dolor sit amet, consectetur, adipisci velit, sed quia non numquam eius modi tempora incidunt ut labore et dolore magnam aliquam quaerat voluptatem, ut enim ad minima veniam, quis nostrum exercitationem ullam corporis suscipit laboriosam, nisi ut aliquid ex ea commodi consequatur.</p>
    <p>Quis autem vel eum iure reprehenderit qui in ea voluptate velit esse quam nihil molestiae consequatur, vel illum qui dolorem eum fugiat quo voluptas nulla pariatur. At vero eos et accusamus et iusto odio dignissimos ducimus qui blanditiis praesentium voluptatum.</p>
  </div>
  <div class="footer-rule"></div>
  <span class="page-number">4</span>
  <div class="offices">London | Dubai | Melbourne | St Helier | Sydney<br><span class="web">www.corvelassociates.net</span></div>
</section>

<!-- Notable individuals / firms -->
<section class="page col-left row-3">
  <h2 class="page-title">NOTABLE<br>INDIVIDUALS / FIRMS</h2>
  <div class="title-rule" style="top:45px"></div>
  <div class="brand brand-small">corvel<br>associates</div>
  <div class="callout">We have highlighted a few individuals and firms that we believe are worth exploring further to determine their level of appropriateness and potential interest in CLIENT:</div>
  <div class="highlight" style="left:19px;top:104px"><span class="numeral">01</span><h3>Heading here</h3><p>Lorem Ipsum is simply dummy text of the printing and typesetting industry.</p></div>
  <div class="highlight" style="left:19px;top:139px"><span class="numeral">02</span><h3>Heading here</h3><p>Lorem Ipsum is simply dummy text of the printing and typesetting industry.</p></div>
  <div class="highlight" style="left:19px;top:174px"><span class="numeral">03</span><h3>Heading here</h3><p>Lorem Ipsum is simply dummy text of the printing and typesetting industry.</p></div>
  <div class="highlight" style="left:158px;top:105px"><span class="numeral">04</span><h3>Heading here</h3><p>Lorem Ipsum is simply dummy text of the printing and typesetting industry.</p></div>
  <div class="highlight" style="left:158px;top:140px"><span class="numeral">05</span><h3>Heading here</h3><p>Lorem Ipsum is simply dummy text of the printing and typesetting industry.</p></div>
  <div class="highlight" style="left:158px;top:175px"><span class="numeral">06</span><h3>Heading here</h3><p>Lorem Ipsum is simply dummy text of the printing and typesetting industry.</p></div>
  <div class="footer-rule"></div>
  <span class="page-number">5</span>
  <div class="offices">London | Dubai | Melbourne | St Helier | Sydney<br><span class="web">www.corvelassociates.net</span></div>
</section>

<!-- Varnsby -->
<section class="page col-right row-3">
  <h2 class="page-title firm">Varnsby</h2>
  <div class="title-rule" style="top:28px"></div>
  <div class="brand brand-small">corvel<br>associates</div>

  <article class="candidate" style="top:42px">
    <div class="portrait" role="img" aria-label="Candidate portrait photo"></div>
    <div class="candidate-name">CANDIDATE A</div>
    <div class="candidate-role">Partner</div>
    <div class="candidate-location">Sydney</div>
    <div class="candidate-bio">
      <p>Candidate A has been a Tax Partner with Varnsby since 2005, having joined the firm as a Graduate in 1993. She is a financial services specialist.</p>
      <p>Candidate A holds a Bachelor of Commerce and a Masters of Taxation from a leading local university.</p>
    </div>
  </article>

  <article class="candidate" style="top:95px">
    <div class="portrait" role="img" aria-label="Candidate portrait photo"></div>
    <div class="candidate-name">CANDIDATE B</div>
    <div class="candidate-role">Partner</div>
    <div class="candidate-location">Sydney</div>
    <div class="candidate-bio">
      <p>Candidate B is a partner at Varnsby with over 13 years of experience as a tax adviser to investment management, infrastructure, private equity and real estate clients.</p>
      <p>Candidate B has extensive experience advising clients throughout the fund life cycle, including fund establishment, acquisitions, due diligence, structuring, financing, divestments, ongoing tax compliance and dealings with revenue authorities.</p>
    </div>
  </article>

  <article class="candidate" style="top:149px">
    <div class="portrait" role="img" aria-label="Candidate portrait photo"></div>
    <div class="candidate-name">CANDIDATE A</div>
    <div class="candidate-role">Partner</div>
    <div class="candidate-location">Sydney</div>
    <div class="candidate-bio">
      <p>Candidate C is a Partner in the tax division of Varnsby in Sydney, and has been with the firm since 2013.</p>
      <p>Candidate C has extensive experience in providing local tax advice, gained in international accounting and law firms, his own firm, and time with a leading infrastructure advisory team.</p>
      <p>Candidate C mainly advises large corporate clients, particularly on infrastructure transactions, M&amp;A, capital management, funds management, banking transactions and tax disputes.</p>
    </div>
  </article>

  <div class="footer-rule"></div>
  <span class="page-number">6</span>
  <div class="offices">London | Dubai | Melbourne | St Helier | Sydney<br><span class="web">www.corvelassociates.net</span></div>
</section>

<!-- QO -->
<section class="page col-left row-4">
  <h2 class="page-title firm">QO</h2>
  <div class="title-rule" style="top:28px"></div>
  <div class="brand brand-small">corvel<br>associates</div>

  <article class="candidate" style="top:42px">
    <div class="portrait" role="img" aria-label="Candidate portrait photo"></div>
    <div class="candidate-name">CANDIDATE A</div>
    <div class="candidate-role">Partner</div>
    <div class="candidate-location">Sydney</div>
    <div class="candidate-bio">
      <p>Candidate A has been a Tax Partner with QO since 2005, having joined the firm as a Graduate in 1993. She is a financial services specialist.</p>
      <p>Candidate A holds a Bachelor of Commerce and a Masters of Taxation from a leading local university.</p>
    </div>
  </article>

  <article class="candidate" style="top:95px">
    <div class="portrait" role="img" aria-label="Candidate portrait photo"></div>
    <div class="candidate-name">CANDIDATE B</div>
    <div class="candidate-role">Partner</div>
    <div class="candidate-location">Sydney</div>
    <div class="candidate-bio">
      <p>Candidate B is a partner at QO with over 13 years of experience as a tax adviser to investment management, infrastructure, private equity and real estate clients.</p>
      <p>Candidate B has extensive experience advising clients throughout the fund life cycle, including fund establishment, acquisitions, due diligence, structuring, financing, divestments, ongoing tax compliance and dealings with revenue authorities.</p>
    </div>
  </article>

  <article class="candidate" style="top:149px">
    <div class="portrait" role="img" aria-label="Candidate portrait photo"></div>
    <div class="candidate-name">CANDIDATE A</div>
    <div class="candidate-role">Partner</div>
    <div class="candidate-location">Sydney</div>
    <div class="candidate-bio">
      <p>Candidate C is a Partner in the tax division of QO in Sydney, and has been with the firm since 2013.</p>
      <p>Candidate C has extensive experience in providing local tax advice, gained in international accounting and law firms, his own firm, and time with a leading infrastructure advisory team.</p>
      <p>Candidate C mainly advises large corporate clients, particularly on infrastructure transactions, M&amp;A, capital management, funds management, banking transactions and tax disputes.</p>
    </div>
  </article>

  <div class="footer-rule"></div>
  <span class="page-number">7</span>
  <div class="offices">London | Dubai | Melbourne | St Helier | Sydney<br><span class="web">www.corvelassociates.net</span></div>
</section>

<!-- Closing -->
<section class="page closing col-right row-4">
  <div class="sketch closing-sketch" role="img" aria-label="Watercolour sketch of a domed railway station with a vintage tram in front"></div>
  <p class="closing-title">Thank you for<br>watching!</p>
  <div class="brand brand-large">corvel<br>associates</div>
</section>

</body>
</html>
```